Web Application Graphic Design Project

We need a design for an online literacy application. The target audience are 9-12 year old children and the application will teach them literacy skills, like essay writing. It is a web-based application called Lumorival and the software developers now need a graphic design to implement into the code - no coding required, just design of the layout.
Wireframes are attached to give an overview of what the functionalities are - it runs in any ordinary web-browser (indicated in the wireframes as well). The application consists of a static background (workspace) onto which individual boxes are added as the student progresses through the tasks. A task panel on the left hand side allows the user to select a task, upon which a popup window will slide open on the right where they enter content. This content is then displayed on the workspace in the background in a box (which can be moved around to organise, seen in frame 3 ). Additional icons on left and right lead to new tasks.
Updates
The wireframe mockup of the application has been updated - please ignore the previous one, which has now been deleted. This is the final version to work from.
Reason: Would like to give more time to allow for a design that meets the young children target audience and for more creative ways for icons and colour schemes.
Reason: We are waiting for some further submissions to come through.
Target Market(s)
9-12 year old school children, so the design should be appealing to both boys and girls.
Industry/Entity Type
Graphic Design
Look and feel
Each slider illustrates characteristics of the customer's brand and the style your logo design should communicate.

```html
<!DOCTYPE html>
<html lang="en">
<head>
<meta charset="utf-8">
<title>Lumorival – Essay Writing</title>
<link rel="stylesheet" href="https://fonts.googleapis.com/css2?family=Open+Sans:wght@400;600;700&display=swap">
<style>
:root{
  --bg:#ffffff;
  --grid:#eef0f2;
  --panel:#ffffff;
  --panel-edge:#cfd3d6;
  --ink:#111111;
  --ink-soft:#333333;
  --box-line:#333333;
  --muted:#9a9ea3;
  --tick:#2fae2f;
  --blue:#3b78c8;
  --star:#f7c21b;
  --red:#d8241d;
  --scroll:#c4c4c4;
}
*{box-sizing:border-box;margin:0;padding:0}
html,body{width:1200px;height:779px;overflow:hidden;background:var(--bg);font-family:"Open Sans",Arial,sans-serif;color:var(--ink)}
.workspace{
  position:absolute;left:0;top:0;width:1280px;height:831px;
  transform:scale(.9375);transform-origin:0 0;
  background-color:var(--bg);
  background-image:linear-gradient(var(--grid) 1px,transparent 1px),linear-gradient(90deg,var(--grid) 1px,transparent 1px);
  background-size:10px 10px;
}
.abs{position:absolute}
.tool{position:absolute;width:70px;text-align:center;font-size:11px;color:var(--ink)}
.tool svg,.tool .avatar{display:block;margin:0 auto 2px}
.avatar{width:34px;height:40px;border-radius:17px 17px 6px 6px;background:linear-gradient(#d9843a,#c0392b 60%,#2b2f36)}

.panel{position:absolute;background:var(--panel);border:1px solid var(--panel-edge);box-shadow:0 0 4px rgba(0,0,0,.15)}
.task-panel{left:78px;top:51px;width:256px;height:736px}
.levels{position:absolute;top:16px;left:0;width:100%}
.level{position:absolute;width:70px;text-align:center;font-size:11px}
.level svg{display:block;margin:0 auto 4px;height:40px}
.task-title{position:absolute;left:11px;top:92px;font-size:20px;font-weight:400;letter-spacing:.2px}
.task-list{list-style:none;position:absolute;left:31px;top:128px;width:200px;font-size:14px}
.task-list li{height:30px;line-height:22px;position:relative}
.task-list li.sub{padding-left:19px}
.task-list .tick{position:absolute;right:-3px;top:0}

.idea-box{position:absolute;background:#fff;border:3px solid var(--box-line);border-radius:3px;font-size:20px;line-height:28px}
.idea-box h2{position:absolute;top:-17px;font-size:20px;font-weight:400;background:#fff;padding:0 2px;line-height:28px}
.teacher-box{left:352px;top:161px;width:351px;height:123px;padding:14px 0 0 17px}
.teacher-box h2{left:33px}
.decode-box{left:525px;top:252px;width:400px;height:142px;padding:14px 0 0 17px;line-height:37px}
.decode-box h2{left:34px}
.ideas-box{left:698px;top:380px;width:300px;height:178px;padding:13px 0 0 6px;font-size:20px;line-height:25px}
.ideas-box h2{left:34px}
.ideas-box ul{list-style:none}
.ideas-box li{padding-left:13px;position:relative}
.ideas-box li::before{content:"•";position:absolute;left:0}

.reference{left:855px;top:51px;width:336px;height:736px;z-index:2}
.reference h2{position:absolute;top:11px;width:100%;text-align:center;font-size:18px;font-weight:400}
.close{position:absolute;right:11px;top:10px}
.search{position:absolute;left:28px;top:41px;width:280px;height:29px;border:1px solid #c9cdd1;border-radius:15px;background:linear-gradient(#f3f4f5,#fff);font-size:12px;color:#aab0b5;padding:6px 0 0 31px}
.search svg{position:absolute;left:11px;top:8px}
.ref-list-frame{position:absolute;left:5px;top:78px;width:325px;height:642px;border:1px solid #a9adb1}
.ref-list{list-style:none;position:absolute;left:10px;top:5px;font-size:15px}
.ref-list li{position:relative;padding-left:18px;height:24px;line-height:20px}
.ref-list li svg.doc{position:absolute;left:0;top:2px}
.ref-list .media{position:absolute;left:218px;top:3px}
.scrollbar{position:absolute;right:4px;top:6px;width:15px;height:632px;border-radius:8px;background:var(--scroll)}
.scrollbar::before{content:"";position:absolute;left:0;top:14px;width:15px;height:116px;background:#f4f4f4;border:1px solid #d0d0d0;border-radius:3px}
</style>
</head>
<body>
<main class="workspace">

  <!-- left tools -->
  <div class="tool" style="left:0;top:75px">
    <svg width="40" height="36" viewBox="0 0 40 36"><path d="M6 30 L10 20 L30 2 L37 9 L17 27 Z" fill="#f2a23a" stroke="#9b5b16"/><path d="M6 30 L10 20 L17 27 Z" fill="#f3d9a8"/><path d="M28 4 L35 11" stroke="#e56a8a" stroke-width="4"/></svg>
    Lesson
  </div>
  <div class="tool" style="left:0;top:164px">
    <svg width="44" height="42" viewBox="0 0 44 42"><rect x="3" y="2" width="38" height="38" rx="3" fill="#2d3640"/><path d="M9 8 H21 V34 H9 Z M23 8 H35 V34 H23 Z" fill="#fff"/><path d="M17 8 V17 L19 15 L21 17 V8" fill="#2d3640"/></svg>
    Activities
  </div>

  <!-- task panel -->
  <aside class="panel task-panel">
    <div class="levels">
      <div class="level" style="left:16px">
        <svg width="30" height="40" viewBox="0 0 30 40"><text x="15" y="34" text-anchor="middle" font-family="Open Sans, Arial, sans-serif" font-size="40" font-weight="700" fill="#111">B</text></svg>Newbie
      </div>
      <div class="level" style="left:98px">
        <svg width="40" height="40" viewBox="0 0 40 40"><path d="M6 30 L24 12 L18 6 H36 V24 L30 18 L12 36 Z" fill="var(--blue)" stroke="#1f4f8e"/></svg>Developer
      </div>
      <div class="level" style="left:178px">
        <svg width="40" height="40" viewBox="0 0 40 40"><path d="M20 2 L25 14 L38 15 L28 24 L31 37 L20 30 L9 37 L12 24 L2 15 L15 14 Z" fill="var(--star)" stroke="#d99a00"/></svg>Star
      </div>
    </div>
    <h1 class="task-title">ESSAY WRITING</h1>
    <ul class="task-list">
      <li>Overview<svg class="tick" width="22" height="20" viewBox="0 0 22 20"><path d="M2 11 L8 17 L20 3" fill="none" stroke="var(--tick)" stroke-width="4"/></svg></li>
      <li>The Question<svg class="tick" width="22" height="20" viewBox="0 0 22 20"><path d="M2 11 L8 17 L20 3" fill="none" stroke="var(--tick)" stroke-width="4"/></svg></li>
      <li class="sub">Teacher-Set Q<svg class="tick" width="22" height="20" viewBox="0 0 22 20"><path d="M2 11 L8 17 L20 3" fill="none" stroke="var(--tick)" stroke-width="4"/></svg></li>
      <li class="sub">Your own Q</li>
      <li class="sub">Pick a Q</li>
      <li>Decoding the Q</li>
      <li>Your Ideas</li>
      <li>Structure</li>
      <li>Writing</li>
      <li>Review</li>
    </ul>
  </aside>

  <!-- workspace boxes -->
  <section class="idea-box teacher-box">
    <h2>Teacher-Set Question</h2>
    <p>How has the internet changed<br>our perception of the nature of<br>information ?</p>
  </section>
  <section class="idea-box decode-box">
    <h2>Decoding the Question</h2>
    <p>Opinion - How ?<br>Research - perceptions<br>Facts - information</p>
  </section>
  <section class="idea-box ideas-box">
    <h2>My Ideas</h2>
    <ul>
      <li>Quality - Better information, more</li>
      <li>Quantity - more information</li>
      <li>Search - finding information is fast</li>
    </ul>
  </section>

  <!-- reference panel -->
  <aside class="panel reference">
    <h2>REFERENCE</h2>
    <svg class="close" width="18" height="18" viewBox="0 0 18 18"><path d="M3 3 L15 15 M15 3 L3 15" stroke="#9a9ea3" stroke-width="4"/></svg>
    <div class="search"><svg width="12" height="12" viewBox="0 0 12 12"><circle cx="5" cy="5" r="3.5" fill="none" stroke="#aab0b5" stroke-width="1.5"/><path d="M7.5 7.5 L11 11" stroke="#aab0b5" stroke-width="1.5"/></svg>Search...</div>
    <div class="ref-list-frame">
      <ul class="ref-list">
        <li style="height:24px"><svg class="doc" width="12" height="15" viewBox="0 0 12 15"><path d="M1 1 H8 L11 4 V14 H1 Z" fill="#dbe8f7" stroke="#7aa3d3"/></svg>Apostrophe</li>
        <li><svg class="doc" width="12" height="15" viewBox="0 0 12 15"><path d="M1 1 H8 L11 4 V14 H1 Z" fill="#dbe8f7" stroke="#7aa3d3"/></svg>Argument</li>
        <li><svg class="doc" width="12" height="15" viewBox="0 0 12 15"><path d="M1 1 H8 L11 4 V14 H1 Z" fill="#dbe8f7" stroke="#7aa3d3"/></svg>Clause</li>
        <li><svg class="doc" width="12" height="15" viewBox="0 0 12 15"><path d="M1 1 H8 L11 4 V14 H1 Z" fill="#dbe8f7" stroke="#7aa3d3"/></svg>Comma</li>
        <li style="height:29px"><svg class="doc" width="12" height="15" viewBox="0 0 12 15"><path d="M1 1 H8 L11 4 V14 H1 Z" fill="#dbe8f7" stroke="#7aa3d3"/></svg>Essay</li>
        <li style="height:30px"><svg class="doc" width="12" height="15" viewBox="0 0 12 15"><path d="M1 1 H8 L11 4 V14 H1 Z" fill="#dbe8f7" stroke="#7aa3d3"/></svg>Full Stop</li>
        <li style="height:29px"><svg class="doc" width="12" height="15" viewBox="0 0 12 15"><path d="M1 1 H8 L11 4 V14 H1 Z" fill="#dbe8f7" stroke="#7aa3d3"/></svg>Introduction</li>
        <li style="height:30px"><svg class="doc" width="12" height="15" viewBox="0 0 12 15"><path d="M1 1 H8 L11 4 V14 H1 Z" fill="#dbe8f7" stroke="#7aa3d3"/></svg>Noun</li>
        <li style="height:30px"><svg class="doc" width="12" height="15" viewBox="0 0 12 15"><path d="M1 1 H8 L11 4 V14 H1 Z" fill="#dbe8f7" stroke="#7aa3d3"/></svg>Orientration</li>
        <li style="height:34px"><svg class="doc" width="12" height="15" viewBox="0 0 12 15"><path d="M1 1 H8 L11 4 V14 H1 Z" fill="#dbe8f7" stroke="#7aa3d3"/></svg>Sentence<svg class="media" width="16" height="12" viewBox="0 0 16 12"><rect x="1" y="3" width="14" height="8" rx="1" fill="#bbb" stroke="#777"/><circle cx="8" cy="7" r="2.5" fill="#eee" stroke="#777"/><rect x="5" y="1" width="5" height="2" fill="#777"/></svg></li>
        <li style="height:35px"><svg class="doc" width="12" height="15" viewBox="0 0 12 15"><path d="M1 1 H8 L11 4 V14 H1 Z" fill="#dbe8f7" stroke="#7aa3d3"/></svg>Topic Sentence</li>
        <li><svg class="doc" width="12" height="15" viewBox="0 0 12 15"><path d="M1 1 H8 L11 4 V14 H1 Z" fill="#dbe8f7" stroke="#7aa3d3"/></svg>Paragraph<svg class="media" width="16" height="12" viewBox="0 0 16 12" style="left:215px"><rect x="1" y="3" width="10" height="7" fill="#999"/><path d="M11 6 L15 3 V10 L11 7 Z" fill="#777"/></svg></li>
      </ul>
      <div class="scrollbar"></div>
    </div>
  </aside>

  <!-- right tools -->
  <div class="tool" style="left:1198px;top:16px"><div class="avatar" role="img" aria-label="Student avatar figure"></div>My Name</div>
  <div class="tool" style="left:1198px;top:102px">
    <svg width="38" height="38" viewBox="0 0 38 38"><circle cx="19" cy="19" r="17" fill="#3f8fd8"/><path d="M8 12 Q14 8 18 13 Q16 20 10 20 Z M22 22 Q30 20 30 28 Q24 33 20 28 Z" fill="#6cc06a"/></svg>Reference</div>
  <div class="tool" style="left:1198px;top:182px">
    <svg width="38" height="38" viewBox="0 0 38 38"><rect x="4" y="4" width="28" height="32" rx="2" fill="#dfe9f6" stroke="#3b6fb5"/><path d="M10 14 H26 M10 20 H26 M10 26 H22" stroke="#3b6fb5" stroke-width="2"/></svg>Samples</div>
  <div class="tool" style="left:1198px;top:264px">
    <svg width="38" height="38" viewBox="0 0 38 38"><rect x="4" y="10" width="28" height="26" rx="2" fill="#8a8f94" stroke="#555"/><rect x="10" y="24" width="16" height="10" fill="#eee"/><path d="M14 2 H24 V12 H30 L19 24 L8 12 H14 Z" fill="#3cae3c" stroke="#207a20"/></svg>Save</div>
  <div class="tool" style="left:1198px;top:346px">
    <svg width="38" height="38" viewBox="0 0 38 38"><circle cx="19" cy="19" r="12" fill="#a6abb0" stroke="#6d7277" stroke-width="6" stroke-dasharray="5 4"/><circle cx="19" cy="19" r="6" fill="#fff" stroke="#6d7277"/></svg>Settings</div>
  <div class="tool" style="left:1198px;top:426px">
    <svg width="38" height="38" viewBox="0 0 38 38"><path d="M5 5 L33 33 M33 5 L5 33" stroke="var(--red)" stroke-width="8"/></svg>Exit</div>

</main>
</body>
</html>
```